Recto Verso Audiology Business Card

Business card with a beautiful design on the back. On the Recto you need the following data Vandrell Osko Audiologist Hearing Solutions Hearing Protection Tinnitus Hyperacusis Tel: 0482/37 58 90 Email: On the back, you need something nice like the attached file. The logo "Corra Nube" can be in the center The colors of the Logo can not be changed If possible stay in the same colors as the logo Another solution is to put the logo on the front and have a nice back (A mosaic of small ears, hearing aids or other ..) Thank you _______________________________________________________________ Visit card On the Recto Vandrell Osko Audiologist Hearing Solutions Hearing Protection Tinnitus Hyperacusis Tel: 0482/37 58 90 Email: You can put the logo " Corra Nube "on the Recto of the Verso The colors of the logo can not be changed. If you put the logo on the back, it must be well integrated. On the Verso I need something in the files. something stylish. It's a visit card for an audiologist. You can get ears of hearing aids if you need. Thanks

Target Market(s)

customers

Contact Information for Business Card

Carte de visite standard ou A6

Font styles to use
Serif
Sans Serif

Colors
33a6d7

Requirements
Must have
• the logo and a stylized background.
Nice to have
• It would be nice to have a back side related to audiology (ears, hearing aids etc.)

```html
<!DOCTYPE html>
<html lang="en">
<head>
<meta charset="utf-8">
<title>Corra Nube – Audiology Business Card</title>
<link href="https://fonts.googleapis.com/css2?family=Ubuntu+Condensed&display=swap" rel="stylesheet">
<style>
  :root {
    --backdrop: #e6e3df;
    --card: #272727;
    --card-pattern: #1f3336;
    --teal: #46b6cb;
    --teal-muted: #3f7f8c;
    --ink: #ffffff;
    --rule: #d9d9d9;
  }
  * { box-sizing: border-box; margin: 0; padding: 0; }
  html, body {
    width: 1200px;
    height: 419px;
    overflow: hidden;
    background: var(--backdrop);
    font-family: "Ubuntu Condensed", "Arial Narrow", sans-serif;
  }
  .canvas {
    position: relative;
    width: 1200px;
    height: 419px;
  }
  .card {
    position: absolute;
    top: 68px;
    width: 440px;
    height: 284px;
    background: var(--card);
    border-radius: 3px;
    box-shadow: 0 6px 18px rgba(0,0,0,0.25);
    overflow: hidden;
  }
  .card--verso { left: 115px; }
  .card--recto { left: 645px; }

  .ear-pattern {
    position: absolute;
    inset: 0;
    background: radial-gradient(circle at 50% 50%, #24393c 0%, var(--card-pattern) 60%, #1b2a2c 100%);
  }

  .brand {
    position: absolute;
    display: flex;
    align-items: center;
    gap: 10px;
    color: var(--teal);
    text-transform: uppercase;
    letter-spacing: 1px;
  }
  .brand__mark {
    display: block;
    border: 2px solid var(--teal);
  }
  .card--verso .brand {
    left: 50%;
    top: 50%;
    transform: translate(-50%, -50%);
    background: var(--card);
    padding: 14px 18px;
    font-size: 30px;
  }
  .card--verso .brand__mark { width: 26px; height: 26px; }

  .card--recto .brand {
    left: 50%;
    top: 44px;
    transform: translateX(-50%);
    font-size: 20px;
    gap: 8px;
  }
  .card--recto .brand__mark { width: 18px; height: 18px; }

  .holder {
    position: absolute;
    top: 118px;
    width: 100%;
    text-align: center;
  }
  .holder__name {
    color: var(--teal);
    font-size: 21px;
    text-transform: uppercase;
    letter-spacing: 0.5px;
    line-height: 1;
  }
  .holder__role {
    color: var(--teal-muted);
    font-size: 13px;
    letter-spacing: 0.5px;
    margin-top: 2px;
  }
  .contact {
    position: absolute;
    top: 168px;
    width: 100%;
    text-align: center;
    color: var(--ink);
    font-size: 13px;
    line-height: 1.25;
  }
  .contact__web { letter-spacing: 3px; }

  .services {
    position: absolute;
    left: 0;
    right: 0;
    top: 212px;
    height: 34px;
    border-top: 1px solid var(--rule);
    border-bottom: 1px solid var(--rule);
    display: flex;
    align-items: center;
    justify-content: center;
    color: var(--ink);
    font-size: 13.5px;
    letter-spacing: 0.3px;
  }
</style>
</head>
<body>
<main class="canvas">

  <section class="card card--verso" aria-label="Card back">
    <div class="ear-pattern" role="img" aria-label="Repeating pattern of small teal ear outlines with sound waves on dark background"></div>
    <div class="brand">
      <span class="brand__mark"></span>
      <span class="brand__name">Corra Nube</span>
    </div>
  </section>

  <section class="card card--recto" aria-label="Card front">
    <div class="brand">
      <span class="brand__mark"></span>
      <span class="brand__name">Corra Nube</span>
    </div>
    <div class="holder">
      <p class="holder__name">Vandrell Osko</p>
      <p class="holder__role">Audiologist Hearing</p>
    </div>
    <div class="contact">
      <p class="contact__line">(P) 0482/37 58 90 &nbsp;(E) info@corranube.com</p>
      <p class="contact__web">www.corranube.com</p>
    </div>
    <p class="services">Solutions Hearing | Protection | Tinnitus | Hyperacusis</p>
  </section>

</main>
</body>
</html>
```